Give Tall Oak Ridge an Online Presence!

Tall Oak Ridge Property Maintenance is an Australian Owned property maintenance company who needs a stand out online presence.

TOR maintains many buildings and sites and wants to appeal to a corporate professional market with their brand new website. TOR is essentially a handyman service offering all maintenance services to home owners, office managers, real estate agents and strata managers.

The Website:
We need a corporate website that appeals to our broader customer base (property owners, property managers, office managers) the copy is being written by a professional so use filler text for now.

Things that we want:
Home page that sets us apart and appeals to the corporate and residential market. The home page needs to not focus on either the residential or commercial market. The home page should focus on our logo and branding. We have a logo already and it is attached to the brief, please use it and try to consider the colour pallette that goes with it. Whilst we want the site to appear strong and manly it is important to remember that 95% of our customers are female so we need the site to be appealing to women. Women need to believe that we are strong, dependable and trustworthy.
We'd like a quote page and potentially also the ability to get a quote from the home page (please don't put it in if it ruins the overall feel of the home page)
An "about us" page
A contact us page
A blog that's built in (we don't want to link to an external blog)
(overall we'd expect to have 6 or 7 pages total)

The site will also need coding - we expect this to be done in a separate project but need you to consider a few things about the coding side of things.

It needs to be iPhone and iPad compatible.

We'd like you to suggest the best CMS that you would use or if you would suggest not using a CMS please let us know with your submissions.

Target Market(s)

Property owners, office managers and property managers who need maintenance on buildings (So all of them)

Industry/Entity Type

Property Maintenance

Requirements
Must have
• Our Logo
Home page
About Us
Residential
Commercial
Real Estate/Strata
Contact Us/Quote
Blog
Nice to have
• Quote form included in home page
Movement on the home page at least
Should not have
• other logos, too much colour
NO FLASH

```html
<!DOCTYPE html>
<html lang="en">
<head>
<meta charset="utf-8">
<title>Tall Oak Ridge Property Maintenance</title>
<link rel="stylesheet" href="https://fonts.googleapis.com/css2?family=Arimo:wght@400;700&family=Nunito:wght@300;800&family=Roboto+Condensed:ital,wght@0,700;1,400&display=swap">
<style>
:root{
  --orange:#f5821f;
  --orange-deep:#ef5a0c;
  --orange-light:#f8a41f;
  --ink:#151312;
  --text:#4a4a4a;
  --title:#555;
  --rule:#cfcfcf;
  --white:#fff;
  --footer:#1b1b1b;
}
*{margin:0;padding:0;box-sizing:border-box}
html,body{width:1200px;height:1196px;overflow:hidden}
body{position:relative;background:#fff;font-family:"Arimo",Arial,sans-serif;color:var(--text)}
.abs{position:absolute}

/* navigation */
.topbar{left:0;top:0;width:1200px;height:46px;background:linear-gradient(#2c2c2c,#0b0b0b)}
.nav{left:125px;top:0;display:flex;height:46px}
.nav a{display:flex;align-items:center;justify-content:center;height:46px;border-left:1px solid #3a3a3a;border-right:1px solid #000;
  color:var(--white);text-decoration:none;font-family:"Roboto Condensed",sans-serif;font-weight:700;font-size:11px;text-transform:uppercase}
.search{left:918px;top:10px;width:187px;height:24px;border-radius:5px;background:linear-gradient(#111,#262626);border:1px solid #444;
  font-size:10px;color:#888;padding:5px 20px 0 0;text-align:right}
.search svg{position:absolute;left:12px;top:4px}

/* hero */
.hero{left:0;top:46px;width:1200px;height:372px;background:radial-gradient(ellipse 380px 300px at 230px 170px,#fbc21c 0%,var(--orange-light) 35%,rgba(248,164,31,0) 70%),linear-gradient(180deg,var(--orange-deep) 0%,var(--orange) 45%,var(--orange-light) 100%)}
.brand{left:110px;top:260px;width:265px;text-align:center;color:var(--white);font-family:"Nunito",sans-serif;font-weight:800;font-size:18px;line-height:21px;text-transform:uppercase;white-space:nowrap}
.brand-mark{left:235px;top:232px;width:14px;height:14px;border-radius:50%;background:var(--white)}
.hero h1{left:453px;font-family:"Nunito",sans-serif;font-weight:800;font-size:32px;letter-spacing:-1px;color:var(--white);white-space:nowrap}
.hero p{left:453px;width:405px;font-family:"Nunito",sans-serif;font-weight:300;font-size:22.5px;line-height:29px;color:var(--white)}
.skyline{left:0;top:330px;width:1200px;height:88px;background:linear-gradient(180deg,rgba(21,19,18,0) 0%,rgba(21,19,18,.55) 40%,var(--ink) 80%)}

/* content */
.content-bg{left:0;top:418px;width:1200px;height:220px;background:linear-gradient(#dcdcdc,#fff 60px)}
.section-title{font-family:"Roboto Condensed",sans-serif;font-style:italic;font-weight:400;font-size:20px;color:var(--title);white-space:nowrap}
.section-title span{color:var(--orange)}
.rule{height:0;border-top:1px dotted var(--rule)}
.vrule{left:753px;top:490px;height:543px;border-left:1px dotted #bbb}

.service-thumb{width:112px;height:85px;box-shadow:0 3px 3px rgba(0,0,0,.2);border-bottom:2px solid #eee}
.service h3{font-size:12.5px;font-weight:400;letter-spacing:.6px;color:var(--title)}
.service p{margin-top:19px;font-size:11px;line-height:14px;color:#5a5a5a;width:440px}

.guarantee{width:250px;height:160px;list-style:none}
.guarantee li{position:absolute;left:0;width:250px;display:flex;align-items:center;font-size:12.5px;letter-spacing:.6px;color:var(--title);height:14px;white-space:nowrap}
.dot{flex:0 0 12px;width:12px;height:12px;border-radius:50%;background:radial-gradient(circle at 40% 35%,#ffe160,#f4b000 60%,#d88d00);margin-right:16px;box-shadow:0 0 0 1px #c28300}
.guarantee a{color:var(--orange);font-weight:700;margin-left:4px}

.contact-info{left:835px;top:835px;font-size:12.5px;line-height:14.5px;letter-spacing:.6px;color:#3c3c3c;font-weight:700;white-space:nowrap}
.contact-info p+p{margin-top:14px}
.btn{top:971px;width:61px;height:24px;border-radius:12px;color:var(--white);font-size:11.5px;display:flex;align-items:center;justify-content:center;text-decoration:none}
.btn-dark{left:833px;background:linear-gradient(#3a3a3a,#0e0e0e)}
.btn-orange{left:904px;background:linear-gradient(var(--orange-light),var(--orange-deep))}

/* footer */
.foot-fade{left:0;top:1040px;width:1200px;height:44px;background:linear-gradient(#fff,#dcdcdc)}
.footer{left:0;top:1084px;width:1200px;height:112px;background:linear-gradient(#2a2a2a,#0d0d0d 70%);border-top:3px solid #555}
.footer-nav{left:190px;top:1109px;display:flex;height:30px}
.footer-nav a{display:flex;align-items:center;padding:0 27px;color:#ddd;text-decoration:none;font-size:10px;letter-spacing:1px;text-transform:uppercase;border-right:1px solid #3a3a3a}
.footer-nav a:last-child{border-right:0}
</style>
</head>
<body>

<header>
  <div class="abs topbar"></div>
  <nav class="abs nav">
    <a href="#" style="width:94px">Home</a>
    <a href="#" style="width:115px">About Us</a>
    <a href="#" style="width:126px">Residential</a>
    <a href="#" style="width:113px">Commercial</a>
    <a href="#" style="width:117px">Real Estate</a>
    <a href="#" style="width:116px">Contact Us</a>
  </nav>
  <div class="abs search">
    <svg width="16" height="16" viewBox="0 0 16 16"><circle cx="9.5" cy="6.5" r="4.5" fill="#bde3f5" stroke="#ddd" stroke-width="1.5"/><line x1="6" y1="10" x2="2" y2="14" stroke="#c9a05a" stroke-width="3" stroke-linecap="round"/></svg>
    search...
  </div>
</header>

<section class="abs hero">
  <h1 class="abs" style="top:58px">We are Tall Oak Ridge</h1>
  <p class="abs" style="top:128px">Our goal is to connect people in search of quality property maintenance both for residential and commercial clients.</p>
</section>
<div class="abs brand-mark"></div>
<div class="abs brand">Tall Oak Ridge<br>Property Maintenance</div>
<div class="abs skyline" role="img" aria-label="Dark city skyline silhouette along the bottom of the banner"></div>

<main>
  <div class="abs content-bg"></div>

  <h2 class="abs section-title" style="left:130px;top:455px">Residential <span>Services</span></h2>
  <div class="abs rule" style="left:130px;top:490px;width:467px"></div>
  <div class="abs vrule"></div>

  <div class="abs service-thumb" style="left:130px;top:523px;background:linear-gradient(#4b8fd6,#9bb 55%,#4c7a3a)" role="img" aria-label="Photo of a suburban house with driveway"></div>
  <div class="abs service" style="left:265px;top:525px"><h3>Residential Services</h3><p>Lorem ipsum dolor sit amet, pri ei illud etiam latine. Ne has inimicus praesent persequeris, at apeirian disputando intellegebat his. Ad saepe integre menan-</p></div>

  <div class="abs service-thumb" style="left:130px;top:650px;background:linear-gradient(135deg,#c9c9c9,#8a8a8a 60%,#e2d6cc)" role="img" aria-label="Photo of a plumber repairing a kitchen sink"></div>
  <div class="abs service" style="left:266px;top:652px"><h3>Residential Services</h3><p>Lorem ipsum dolor sit amet, pri ei illud etiam latine. Ne has inimicus praesent persequeris, at apeirian disputando intellegebat his. Ad saepe integre menan-</p></div>

  <div class="abs service-thumb" style="left:130px;top:776px;background:linear-gradient(135deg,#e8c24a,#b9a98a 40%,#6d5a45)" role="img" aria-label="Photo of an electrician working on a switchboard"></div>
  <div class="abs service" style="left:266px;top:778px"><h3>Residential Services</h3><p>Lorem ipsum dolor sit amet, pri ei illud etiam latine. Ne has inimicus praesent persequeris, at apeirian disputando intellegebat his. Ad saepe integre menan-</p></div>

  <div class="abs service-thumb" style="left:130px;top:905px;background:linear-gradient(135deg,#b77d45,#d8a968 50%,#6b7fa0)" role="img" aria-label="Photo of hands measuring timber with a tape"></div>
  <div class="abs service" style="left:266px;top:908px"><h3>Residential Services</h3><p>Lorem ipsum dolor sit amet, pri ei illud etiam latine. Ne has inimicus praesent persequeris, at apeirian disputando intellegebat his. Ad saepe integre menan-</p></div>

  <aside>
    <h2 class="abs section-title" style="left:834px;top:451px">Our <span>Guarantee</span></h2>
    <div class="abs rule" style="left:830px;top:490px;width:228px"></div>
    <ul class="abs guarantee" style="left:833px;top:520px">
      <li style="top:0"><span class="dot"></span>Professional service</li>
      <li style="top:37px"><span class="dot"></span>Knowledgeable</li>
      <li style="top:73px"><span class="dot"></span>Wide range of services</li>
      <li style="top:111px"><span class="dot"></span>Affordable prices - <a href="#">contact us!</a></li>
      <li style="top:146px"><span class="dot"></span>Proudly serving since 2005</li>
    </ul>

    <h2 class="abs section-title" style="left:834px;top:762px">Contact <span>Us</span></h2>
    <div class="abs rule" style="left:830px;top:803px;width:228px"></div>
    <div class="abs contact-info">
      <p>City Name, Australia<br>42-44 Harbour Lane<br>Central, Sydney</p>
      <p>tor@mailbox.test</p>
      <p>0800 418552<br>0800 418553</p>
    </div>
    <a class="abs btn btn-dark" href="#">contact</a>
    <a class="abs btn btn-orange" href="#">quote</a>
  </aside>
</main>

<footer>
  <div class="abs foot-fade"></div>
  <div class="abs footer"></div>
  <nav class="abs footer-nav">
    <a href="#">About Us</a>
    <a href="#">Residential</a>
    <a href="#">Commercial</a>
    <a href="#">Real Estate/Strata</a>
    <a href="#">Contact Us/Quote</a>
    <a href="#">Blog</a>
  </nav>
</footer>

</body>
</html>
```